Illustrate a statistic and its significance

Please create a graphical representation of the success rate of the Vail Procedure for our website. The Vail Procedure has a success rate of 80%. This means the procedure is successful for 8 out of every 10 people. An 80% success rate by itself is great. However, it's even more impressive when you consider that the only people we perform this procedure on are patients who have exhausted conventional treatment options for migraines and headaches. I would really like to emphasize both the success rate and the type of patients we are successful in treating with this procedure.
For example, you could create an illustration of outlines of 10 people with 8 of them shaded in, which would represent an 80% success rate. Then, underneath this image, you could add a bullet list of the types of treatments patients (such as the 10 figures in the image) have tried before coming to us/having this procedure, which include the following:
Prescription medications
Trigger point injections
Nerve blocks
Migraine surgery
Dermil
Chiropractic care
Physical therapy
Biofeedback
Massage
Acupuncture
Or maybe there is another/better way to represent this statistic graphically? I'm just looking for an effective illustration of this important statistic and its significance.
Our brand colors are red (#fd444a) and blue (#214170)
Thank you!
People who suffer from chronic migraines and headaches
Healthcare/Medical
- Athiti

```html
<!DOCTYPE html>
<html lang="en">
<head>
<meta charset="UTF-8">
<title>Vail Procedure Success Rate</title>
<link rel="stylesheet" href="https://fonts.googleapis.com/css2?family=Montserrat:wght@700&display=swap">
<style>
  :root {
    --brand-red: #fd444a;
    --brand-blue: #214170;
    --paper: #ffffff;
  }
  html, body {
    margin: 0;
    padding: 0;
    overflow: hidden;
    background: var(--paper);
  }
  .canvas {
    position: relative;
    width: 1200px;
    height: 1000px;
    overflow: hidden;
    background: var(--paper);
    font-family: "Montserrat", Arial, sans-serif;
    color: var(--brand-blue);
  }
  .success-wheel {
    position: absolute;
    left: 0;
    top: 0;
    width: 1200px;
    height: 1000px;
  }
  .wheel-base { fill: var(--brand-blue); }
  .wheel-success { fill: var(--brand-red); }
  .wheel-gap { stroke: var(--paper); stroke-width: 22; }
  .wheel-center { fill: var(--paper); }

  .treatment-list {
    list-style: none;
    margin: 0;
    padding: 0;
  }
  .treatment {
    position: absolute;
    display: flex;
    align-items: flex-start;
    gap: 9px;
    font-size: 15.5px;
    font-weight: 700;
    line-height: 25px;
    letter-spacing: 0.3px;
    text-transform: uppercase;
    text-align: center;
    white-space: nowrap;
  }
  .treatment::before {
    content: "";
    flex: none;
    width: 6px;
    height: 6px;
    margin-top: 9px;
    border-radius: 50%;
    background: var(--brand-red);
  }
  .t-trigger      { left: 519px; top: 313px; }
  .t-nerve        { left: 519px; top: 403px; }
  .t-prescription { left: 360px; top: 450px; }
  .t-dermil       { left: 557px; top: 468px; }
  .t-chiro        { left: 673px; top: 463px; }
  .t-surgery      { left: 381px; top: 525px; }
  .t-physical     { left: 545px; top: 533px; }
  .t-acupuncture  { left: 673px; top: 538px; }
  .t-biofeedback  { left: 524px; top: 623px; }
  .t-massage      { left: 544px; top: 687px; }

  .headline {
    position: absolute;
    left: 0;
    top: 905px;
    width: 1216px;
    margin: 0;
    text-align: center;
    font-size: 33px;
    font-weight: 700;
    letter-spacing: 0.2px;
    color: var(--brand-blue);
  }
</style>
</head>
<body>
<main class="canvas">
  <svg class="success-wheel" viewBox="0 0 1200 1000" aria-hidden="true">
    <circle class="wheel-base" cx="598" cy="508" r="380"/>
    <path class="wheel-success" d="M598 508 L374.6 200.6 A380 380 0 0 1 821.4 200.6 Z"/>
    <g class="wheel-gaps">
      <line class="wheel-gap" x1="598" y1="100" x2="598" y2="916"/>
      <line class="wheel-gap" x1="833.1" y1="184.4" x2="362.9" y2="831.6"/>
      <line class="wheel-gap" x1="978.4" y1="384.4" x2="217.6" y2="631.6"/>
      <line class="wheel-gap" x1="978.4" y1="631.6" x2="217.6" y2="384.4"/>
      <line class="wheel-gap" x1="833.1" y1="831.6" x2="362.9" y2="184.4"/>
    </g>
    <rect class="wheel-center" x="503" y="250" width="190" height="518"/>
    <rect class="wheel-center" x="343" y="411" width="510" height="195"/>
  </svg>

  <ul class="treatment-list">
    <li class="treatment t-trigger">Trigger point<br>injections</li>
    <li class="treatment t-nerve">Nerve blocks</li>
    <li class="treatment t-prescription">Prescription<br>medications</li>
    <li class="treatment t-dermil">Dermil</li>
    <li class="treatment t-chiro">Chiropractic<br>care</li>
    <li class="treatment t-surgery">Migraine<br>surgery</li>
    <li class="treatment t-physical">Physical<br>therapy</li>
    <li class="treatment t-acupuncture">Acupuncture</li>
    <li class="treatment t-biofeedback">Biofeedback</li>
    <li class="treatment t-massage">Massage</li>
  </ul>

  <p class="headline">The Vail Procedure has an 80% success rate.</p>
</main>
</body>
</html>
```